Co-Living Retreat Centre Pitch Deck

We are needing fresh new pitch deck for our Co-Living Retreat Centre project. We are building a 40 unit community focused on personal development and holistic living!

Here is the branding guide:
https://www.plorvex.com/sheet/QWRT8mHkzp3/vbLoPnXaTd_4uR-7eWsMqY/open

Here is the Content:
https://files.tamberlo.com/store/boxes/8K4Pm2vRtXw7nQ91bLzHyE5cJd3sFa0Gq?mode=viewing

Target Market(s)

30-45 Year olds that are into Yoga, Meditation, Personal Development, Balance Lifestyle.

Font styles to use
Serif
Sans Serif

Requirements
Must have
• Must have the colours from our branding.
Nice to have
• Have some elements of nature, Inspiration,

```html
<!DOCTYPE html>
<html lang="en">
<head>
<meta charset="utf-8">
<title>The Fernhaven – Pitch Deck</title>
<link rel="stylesheet" href="https://fonts.googleapis.com/css2?family=Archivo:wght@700;800&family=Nunito+Sans:wght@400;800&display=swap">
<style>
  :root {
    --bg-dark: #38383a;
    --bg-light: #47474a;
    --green: #6a8f6c;
    --green-mid: #4f7d55;
    --green-dark: #2f6040;
    --heading: #2f5a3a;
    --text: #1f1f1f;
    --white: #ffffff;
  }
  * { margin: 0; padding: 0; box-sizing: border-box; }
  html, body { width: 1200px; height: 2481px; overflow: hidden; }
  body { background: var(--bg-dark); position: relative; font-family: "Nunito Sans", sans-serif; }
  .backdrop { position: absolute; inset: 0; }
  .slide {
    position: absolute; left: 129px; width: 941px; height: 705px;
    background: var(--white); overflow: hidden;
    box-shadow: 6px 8px 10px rgba(0,0,0,.55);
  }
  .slide--cover { top: 128px; }
  .slide--vision { top: 888px; }
  .slide--problem { top: 1648px; }
  .slide__shapes { position: absolute; inset: 0; }
  .cover__title {
    position: absolute; left: 46px; top: 106px;
    font-family: "Archivo", sans-serif; font-weight: 800; font-size: 64px;
    letter-spacing: 1px; color: var(--white); line-height: 1;
  }
  .cover__tagline {
    position: absolute; left: 50px; top: 202px; width: 300px;
    font-family: "Nunito Sans", sans-serif; font-weight: 800; font-size: 26px;
    line-height: 34px; color: var(--white);
  }
  .site-url {
    position: absolute; top: 632px; height: 46px; line-height: 46px;
    font-family: "Archivo", sans-serif; font-weight: 700; font-size: 22px;
    letter-spacing: 9.4px; color: var(--white);
  }
  .slide--cover .site-url { left: 315px; }
  .slide--vision .site-url, .slide--problem .site-url { left: 218px; }
  .section-title {
    position: absolute; left: 52px;
    font-family: "Archivo", sans-serif; font-weight: 700; font-size: 30px;
    color: var(--heading); line-height: 1.2;
  }
  .section-body {
    position: absolute; left: 52px; width: 830px;
    font-family: "Nunito Sans", sans-serif; font-weight: 400;
    font-size: 20.5px; line-height: 26.6px; color: var(--text);
  }
</style>
</head>
<body>
  <svg class="backdrop" width="1200" height="2481" viewBox="0 0 1200 2481" aria-hidden="true">
    <polygon points="1200,130 1200,2481 0,2481 0,2230 830,880" fill="var(--bg-light)"/>
  </svg>

  <section class="slide slide--cover">
    <svg class="slide__shapes" width="941" height="705" viewBox="0 0 941 705">
      <defs>
        <linearGradient id="photoTone" x1="0" y1="0" x2="0" y2="1">
          <stop offset="0" stop-color="#b9c7a9"/>
          <stop offset="0.45" stop-color="#6f7f57"/>
          <stop offset="0.75" stop-color="#7fa35a"/>
          <stop offset="1" stop-color="#98b96a"/>
        </linearGradient>
      </defs>
      <rect width="941" height="705" fill="url(#photoTone)" role="img" aria-label="Photo of a woman in a seated side-stretch yoga pose on a mat on grass in a garden"/>
      <polygon points="0,0 578,0 178,705 0,705" fill="var(--green)"/>
      <polygon points="578,0 620,0 220,705 178,705" fill="var(--green-dark)" opacity=".75"/>
      <polygon points="941,345 941,705 735,705" fill="var(--green-mid)"/>
      <polygon points="941,300 941,345 735,705 705,705" fill="var(--green-dark)" opacity=".8"/>
      <polygon points="0,95 690,95 640,182 0,182" fill="var(--green-dark)" opacity=".9"/>
      <polygon points="190,632 895,632 870,678 165,678" fill="var(--green)" opacity=".85"/>
    </svg>
    <h1 class="cover__title">THE FERNHAVEN</h1>
    <p class="cover__tagline">The greatest quest in life is to reach one’s highest potential.</p>
    <p class="site-url">www.maelvoristane.com</p>
  </section>

  <section class="slide slide--vision">
    <svg class="slide__shapes" width="941" height="705" viewBox="0 0 941 705" aria-hidden="true">
      <polygon points="796,0 941,0 941,252" fill="var(--green-dark)"/>
      <polygon points="812,0 941,0 941,224" fill="var(--green-mid)"/>
      <polygon points="77,632 894,632 870,678 49,678" fill="var(--green)"/>
    </svg>
    <h2 class="section-title" style="top:180px">VISION</h2>
    <p class="section-body" style="top:244px">Creating communities and experiences that revolutionize optimal living and evoke transformation. Empowering co-creation passion and purpose to awaken the ultimate self.</p>
    <h2 class="section-title" style="top:353px">MISSION</h2>
    <p class="section-body" style="top:416px">To shape conscious co-living spaces and experiences where facilitators, creatives, entrepreneurs and wanderers alike come together to reach their highest potential. Creating a sanctuary for those who crave growth, connection and self-actualization.</p>
    <p class="site-url">www.maelvoristane.com</p>
  </section>

  <section class="slide slide--problem">
    <svg class="slide__shapes" width="941" height="705" viewBox="0 0 941 705" aria-hidden="true">
      <polygon points="796,0 941,0 941,252" fill="var(--green-dark)"/>
      <polygon points="812,0 941,0 941,224" fill="var(--green-mid)"/>
      <polygon points="77,632 894,632 870,678 49,678" fill="var(--green)"/>
    </svg>
    <h2 class="section-title" style="top:126px">THE PROBLEM</h2>
    <p class="section-body" style="top:183px">Majority of our western civilization has become disconnected from themselves, nature and others. Chasing material possessions in a concrete jungle. Loneliness and stress has become an epidemic.</p>
    <p class="section-body" style="top:281px">People are seeking a place to live and grow in a community of like minded people that inspire and support their growth and passions.</p>
    <h2 class="section-title" style="top:356px">OUR PROMISE</h2>
    <p class="section-body" style="top:413px">Our purpose is to create a transformative hub for change makers seeking personal development and optimal living with a desire to always drive positive change in the world. We inspire people to live a balanced lifestyle that fosters a deeper connection to themselves, others and nature. Creating an optimised way of life that covers all areas of success, health and wealth.</p>
    <p class="site-url">www.maelvoristane.com</p>
  </section>
</body>
</html>
```